International PR and marketing agency needs website design

We need a branding website, for a company based in the US (Washington DC). We are a communication (PR, marketing, social media) agency. We already have the copy, and we have some example websites (some major agencies), that we like.
For example:
https://pellowtrask.example/
https://durnevaleglobal.example/
https://varnok.example/
https://qmf-reach.example/
https://www.thornbury.example/
The website must be a multi-language site, we will add the new languages step-by-step.
We would like to upload content continuously.
The website has to have sub-pages (segments), and news part.
Target Market(s)
Global
Industry/Entity Type
Public relations, Communications, Marketing, Social Media
Number of Pages Required
5+ page
Font styles to use
Other font styles liked:
- Well readable, modern style.
Look and feel

```html
<!DOCTYPE html>
<html lang="en">
<head>
<meta charset="utf-8">
<title>Halcyra — Unique digital ideas</title>
<link href="https://fonts.googleapis.com/css2?family=Rubik:wght@300;400;500;600;700&family=Playfair+Display:ital,wght@1,600;1,700&display=swap" rel="stylesheet">
<style>
:root{
  --magenta:#8e1f7a;
  --red:#e3294b;
  --ink:#16161c;
  --text:#4a4a55;
  --muted:#8a8a95;
  --faint:#d9d9e0;
  --hero:#3d4468;
  --dark:#1b1b1e;
  --white:#ffffff;
  --grad:linear-gradient(90deg,var(--magenta),var(--red));
}
*{box-sizing:border-box;margin:0;padding:0}
html,body{width:1200px;height:4138px;overflow:hidden;background:#fff}
body{position:relative;font-family:'Rubik',sans-serif;color:var(--ink)}
.abs{position:absolute}
.serif{font-family:'Playfair Display',serif;font-style:italic}
.photo{position:absolute}

/* ---------- desktop ---------- */
.desktop{position:absolute;left:14px;top:0;width:1006px;height:4118px;background:#fff;box-shadow:0 0 0 1px #ececf0;overflow:hidden}
.scrollbar{position:absolute;left:1010px;top:0;width:10px;height:4118px;background:#f1f1f3;border-left:1px solid #e2e2e6}
.scrollbar span{position:absolute;left:2px;top:60px;width:5px;height:220px;background:#bdbdc4;border-radius:3px}

.nav{position:absolute;left:0;top:25px;width:1006px;height:63px;background:#fff}
.brand{position:absolute;display:flex;align-items:center;gap:6px;font-weight:600;color:var(--magenta)}
.brand i{display:block;border-radius:50%;background:var(--red)}
.nav .brand{left:21px;top:14px;font-size:18px}
.nav .brand i{width:16px;height:16px}
.nav-links{position:absolute;left:492px;top:22px;display:flex;gap:20px;font-size:11px;color:var(--ink)}
.nav-dot{position:absolute;left:791px;top:18px;width:22px;height:22px;border:1px solid var(--red);border-radius:50%}
.nav-dot::after{content:"";position:absolute;left:8px;top:8px;width:4px;height:4px;border-radius:50%;background:var(--red)}
.btn{position:absolute;display:flex;align-items:center;justify-content:center;gap:6px;border-radius:22px;font-size:10px;font-weight:500}
.btn-grad{background:var(--grad);color:#fff}
.btn-white{background:#fff;color:var(--ink)}
.nav .btn{left:895px;top:12px;width:85px;height:35px;border-radius:2px}

.hero{position:absolute;left:0;top:88px;width:1006px;height:442px;background:linear-gradient(180deg,#2d3352,#4a5278 60%,#5b6488);overflow:hidden}
.hero .wave{position:absolute;left:0;bottom:0}
.hero-kicker{position:absolute;top:118px;width:100%;text-align:center;color:#fff;font-size:8px;font-weight:600;letter-spacing:.5px}
.hero h1{position:absolute;top:140px;width:100%;text-align:center;color:#fff;font-size:66px;font-weight:600;letter-spacing:-1px}
.hero h1 em{font-family:'Playfair Display',serif;font-style:italic;font-weight:700}
.hero p{position:absolute;top:232px;width:100%;text-align:center;color:#e3e5f0;font-size:13px;line-height:1.75}
.hero .btn{top:314px;height:43px}

.about-title{position:absolute;left:127px;top:640px;font-size:30px;line-height:1;font-weight:500}
.benefit{position:absolute;left:127px;width:236px}
.benefit h3{font-size:10px;font-weight:500;color:var(--magenta);margin-bottom:6px}
.benefit p{font-size:8.5px;line-height:1.5;color:var(--text)}
.up-btn{position:absolute;left:940px;top:868px;width:30px;height:30px;border-radius:50%;background:#fff;box-shadow:0 2px 8px rgba(0,0,0,.15)}

.years{position:absolute;left:150px;top:1120px;font-size:170px;font-weight:700;line-height:1}
.years-label{position:absolute;left:132px;top:1298px;font-size:8px;color:var(--ink)}
.badge{position:absolute;background:var(--magenta);color:#fff;border-radius:8px;font-size:6px;padding:3px 6px}
.services-title{position:absolute;left:316px;top:1183px;font-size:40px;line-height:46px;font-weight:400}
.svc-para{position:absolute;width:236px;font-size:8.5px;line-height:1.5;color:var(--text)}
.svc-list{position:absolute;top:1418px;list-style:none;font-size:12px;color:var(--ink)}
.svc-list .cap{font-size:7px;color:var(--muted);margin-bottom:17px;letter-spacing:.3px}
.svc-list li{height:36px}

.spec-title{position:absolute;top:1732px;width:100%;text-align:center;font-size:26px;color:var(--ink)}
.spec-sub{position:absolute;top:1782px;width:100%;text-align:center;font-size:9.5px;line-height:1.7;color:var(--muted)}
.spec-item{position:absolute;left:510px;width:360px}
.spec-item .num{position:absolute;left:0;top:0;width:37px;height:37px;border-radius:50%;background:var(--magenta);color:#fff;font-size:12px;display:flex;align-items:center;justify-content:center;box-shadow:0 0 0 4px #f0dcec}
.spec-item h4{margin-left:65px;font-size:11.5px;font-weight:500;margin-bottom:10px}
.spec-item p{margin-left:65px;font-size:8.5px;line-height:1.9;color:var(--muted)}

.team-title{position:absolute;top:2282px;width:100%;text-align:center;font-size:24px;font-weight:500}
.member{position:absolute;top:2365px;width:197px;height:222px;background:#fff;box-shadow:0 4px 16px rgba(0,0,0,.05)}
.member .photo{left:0;top:0;width:197px;height:194px}
.member .name{position:absolute;left:0;top:178px;font-size:13px;color:#cfd0d8}
.member .role{position:absolute;left:0;top:202px;font-size:9px;color:#c8c9d0}

.video{position:absolute;left:132px;top:2656px;width:735px;height:371px;border-radius:4px;overflow:hidden;box-shadow:0 12px 30px rgba(0,0,0,.15)}
.video .photo{inset:0;background:linear-gradient(160deg,#c9cfd6,#8d97a3 55%,#5d6673)}
.video h3{position:absolute;left:41px;top:214px;width:520px;color:#fff;font-size:21px;line-height:30px;font-weight:500}
.play{position:absolute;left:41px;top:280px;width:38px;height:38px;border-radius:50%;border:1px solid rgba(255,255,255,.7)}
.play svg{position:absolute;left:14px;top:12px}
.video .play-txt{position:absolute;left:91px;top:282px;color:#fff;font-size:8px;line-height:1.9}

.quote{position:absolute;width:369px;background:#fff;box-shadow:0 4px 18px rgba(0,0,0,.07);padding:16px 38px}
.quote h5{font-size:8.5px;font-weight:400;margin-bottom:8px}
.quote p{font-size:8.5px;line-height:1.5;color:var(--text)}
.quote .dot{position:absolute;right:24px;top:16px;width:9px;height:9px;border-radius:50%;background:#2f3a8f}

.blog-kicker{position:absolute;left:581px;top:3131px;font-size:6.5px}
.blog-title{position:absolute;left:581px;top:3153px;font-size:24px;font-weight:500}
.blog-text{position:absolute;left:581px;top:3198px;width:280px;font-size:10.5px;line-height:1.7;color:var(--muted)}
.more{position:absolute;left:581px;top:3306px;width:84px;height:39px;background:var(--grad);color:#fff;font-size:9px;font-weight:500;display:flex;align-items:center;justify-content:center;gap:5px}

.cta{position:absolute;left:0;top:3509px;width:1006px;height:286px;background:linear-gradient(90deg,#7d1d6e,#b11f5b 55%,#e3294b)}
.cta h2{position:absolute;top:95px;width:100%;text-align:center;color:#fff;font-size:27px;line-height:39px;font-weight:500}
.cta h2 em{font-family:'Playfair Display',serif;font-style:italic;font-weight:700}
.cta .btn{top:196px;height:38px;font-size:9px}

.footer{position:absolute;left:0;top:3795px;width:1006px;height:323px;background:var(--dark);color:#fff}
.footer .brand{left:136px;top:88px;font-size:22px;color:#d83a72}
.footer .brand i{width:18px;height:18px}
.fcol{position:absolute;top:81px}
.fcol h6{font-size:10px;font-weight:500;margin-bottom:14px}
.fcol li{list-style:none;font-size:8.5px;color:#85858f;height:22px}
.fcol .small{font-size:7px;color:#85858f;margin-bottom:6px}
.fcol .big{font-size:11px;margin-bottom:24px}
.socials{display:flex;gap:12px}
.socials i{width:16px;height:16px;border-radius:50%;background:#8a8a93;display:block}
.fbottom{position:absolute;top:273px;font-size:7px;color:#85858f}

/* ---------- mobile ---------- */
.mobile{position:absolute;left:1038px;top:25px;width:148px;height:3487px;background:#fff;overflow:hidden;box-shadow:0 0 0 1px #e4e4e8}
.m-hero{position:absolute;left:0;top:0;width:148px;height:302px;background:linear-gradient(180deg,#2d3352,#555e84)}
.m-hero .brand{left:6px;top:6px;font-size:9px;color:#fff}
.m-hero .brand i{width:8px;height:8px}
.m-burger{position:absolute;right:8px;top:10px;width:10px;height:7px;border-top:1.5px solid #fff;border-bottom:1.5px solid #fff}
.m-hero .k{position:absolute;top:36px;width:100%;text-align:center;color:#fff;font-size:4.5px}
.m-hero h1{position:absolute;top:48px;width:100%;text-align:center;color:#fff;font-size:24px;line-height:26px;font-weight:600}
.m-hero h1 em{font-family:'Playfair Display',serif;font-style:italic}
.m-hero p{position:absolute;top:132px;left:14px;width:120px;text-align:center;color:#dde0ec;font-size:5px;line-height:1.5}
.m-hero .btn{left:38px;width:72px;height:15px;font-size:5px}
.m-t{position:absolute;left:8px;font-weight:500}
.m-p{position:absolute;left:8px;width:132px;font-size:4.8px;line-height:1.55;color:var(--text)}
.m-h{position:absolute;left:8px;font-size:5px;font-weight:500;color:var(--magenta)}
.m-li{position:absolute;left:8px;font-size:5.5px}
.m-card{position:absolute;left:8px;width:122px;height:140px;background:#fff;box-shadow:0 2px 8px rgba(0,0,0,.06)}
.m-card .photo{left:0;top:0;width:122px;height:120px}
.m-card span{position:absolute;left:0;top:122px;font-size:5px}
.m-q{position:absolute;left:12px;width:128px;height:50px;background:#fff;box-shadow:0 2px 8px rgba(0,0,0,.07);padding:6px 8px;font-size:4px;line-height:1.5;color:var(--text)}
.m-cta{position:absolute;left:0;top:2905px;width:148px;height:212px;background:linear-gradient(160deg,#7d1d6e,#e3294b)}
.m-foot{position:absolute;left:0;top:3117px;width:148px;height:370px;background:var(--dark);color:#fff}
</style>
</head>
<body>

<div class="desktop">
  <header class="nav">
    <div class="brand"><i></i>Halcyra</div>
    <nav class="nav-links"><span>Home</span><span>Our Services</span><span>About Us</span><span>Blog</span><span>Contact</span></nav>
    <div class="nav-dot"></div>
    <div class="btn btn-grad">Get Started</div>
  </header>

  <section class="hero">
    <div class="photo" role="img" aria-label="Business team working around a laptop in an office, dark blue overlay" style="inset:0;background:linear-gradient(120deg,rgba(40,44,72,.2),rgba(110,118,150,.25))"></div>
    <div class="hero-kicker">LOREM IPSUM IS SIMPLY DUMMY</div>
    <h1>Unique digital <em>ideas.</em></h1>
    <p>Our experts, creative staff and data analysts are up to the most<br>extraordinary challenges on all parts of the world. This is not</p>
    <div class="btn btn-grad" style="left:362px;width:131px">Let's Talk <span>→</span></div>
    <div class="btn btn-white" style="left:501px;width:128px">Get Started <span>→</span></div>
    <svg class="wave" width="1006" height="70" viewBox="0 0 1006 70" preserveAspectRatio="none"><path d="M0 60 C250 30 420 20 560 38 C720 58 860 50 1006 0 L1006 70 L0 70Z" fill="#fff"/></svg>
  </section>

  <section class="about">
    <h2 class="about-title">We are building<br>relationships</h2>
    <div class="benefit" style="top:730px"><h3>Company Benefits</h3><p>Thinking beyond media relations and marketing services, we understand the needs of our clients, and our experts and our creative staff are working on building long-term relationships. Anywhere in the world.</p></div>
    <div class="benefit" style="top:841px"><h3>Philosophy</h3><p>Thinking beyond media relations and marketing services, we understand the needs of our clients, our experts and our creative staff are working on</p></div>
    <div class="benefit" style="top:926px"><h3>Global Solution</h3><p>Thinking beyond media relations and marketing services, we understand the needs of our clients, and our experts and our creative staff are working on building long-term relationships.</p></div>
    <div class="photo" role="img" aria-label="Portrait of a smiling businesswoman in a white shirt" style="left:457px;top:662px;width:339px;height:344px;background:linear-gradient(135deg,#f1ede8,#d9cfc4 55%,#efebe6);box-shadow:0 10px 30px rgba(0,0,0,.12)"></div>
    <div class="up-btn"><svg width="30" height="30"><path d="M12 17l3-3 3 3" fill="none" stroke="#333" stroke-width="1.2"/></svg></div>
  </section>

  <section class="services">
    <div class="years">9</div>
    <div class="years-label">Years of experience</div>
    <div class="badge" style="left:316px;top:1161px">Our Expertise</div>
    <h2 class="services-title">we provide the widest<br>possible range of services.</h2>
    <p class="svc-para" style="left:321px;top:1302px">To make choosing much easier for You, we provide the widest possible range of services. Let it be media relations, crisis management or marketing services, our experts are always available.</p>
    <p class="svc-para" style="left:597px;top:1302px">To make choosing much easier for You, we provide the widest possible range of services. Let it be media relations, crisis management or marketing services, our experts are always available.</p>
    <ul class="svc-list" style="left:321px"><div class="cap">OUR SERVICES</div><li>Consumer Products and Services</li><li>Content &amp; Publishing Strategy</li><li>Crisis Management</li><li>Brand Marketing</li><li>B2B Marketing</li><li>Change Management</li></ul>
    <ul class="svc-list" style="left:597px"><div class="cap">OUR SERVICES</div><li>Data &amp; Analytics</li><li>Public Affairs</li><li>Social Media</li><li>Media Relation</li><li>Technology</li><li>Media Production</li></ul>
  </section>

  <section class="specialities">
    <h2 class="spec-title serif">Other specalities</h2>
    <p class="spec-sub">We provide digital experience services to startups<br>and small businesses.</p>
    <div class="photo" role="img" aria-label="Two business people shaking hands" style="left:177px;top:1871px;width:279px;height:274px;background:linear-gradient(135deg,#2f4f73,#7f9bb8 50%,#c9d6e2)"></div>
    <div class="spec-item" style="top:1852px"><div class="num">1</div><h4>Specialized Pre-Sales</h4><p>Our experts can offer a wide network of relations, from<br>large corporations, through companies producing</p></div>
    <div class="spec-item" style="top:1947px"><div class="num">2</div><h4>Armed Forces</h4><p>We have shown several solutions especially made for<br>armed forces that support IT-infrastructure and are<br>designed to increase data security.</p></div>
    <div class="spec-item" style="top:2058px"><div class="num">3</div><h4>Partnership Management</h4><p>Partnerships never go out of style. Corporations are<br>continuously seeking more and more</p></div>
  </section>

  <section class="team">
    <h2 class="team-title">Leading the best <span class="serif">marketing team.</span></h2>
    <div class="member" style="left:154px"><div class="photo" role="img" aria-label="Portrait of a smiling male team member" style="background:linear-gradient(135deg,#5b7fa6,#3b3a40 60%,#8aa3bd)"></div><div class="name">Lorem Ipsum is</div><div class="role">Lorem Ipsum is simply</div></div>
    <div class="member" style="left:399px"><div class="photo" role="img" aria-label="Portrait of a female team member" style="background:linear-gradient(135deg,#f0ece6,#d8ccbf 55%,#ffffff)"></div><div class="name">Lorem Ipsum is</div><div class="role">Lorem Ipsum is simply</div></div>
    <div class="member" style="left:644px"><div class="photo" role="img" aria-label="Portrait of a male team member in a suit" style="background:linear-gradient(135deg,#e7ecef,#59606a 55%,#cfd7dc)"></div><div class="name">Lorem Ipsum is</div><div class="role">Lorem Ipsum is simply</div></div>
  </section>

  <section class="video">
    <div class="photo" role="img" aria-label="Colleagues discussing work in a bright office"></div>
    <h3>Watch the creative process behind the Our work</h3>
    <div class="play"><svg width="10" height="12"><path d="M0 0L10 6L0 12Z" fill="#fff"/></svg></div>
    <div class="play-txt">Watch video<br>See how it works</div>
  </section>

  <section class="testimonials">
    <div class="quote" style="left:132px;top:3075px"><i class="dot"></i><h5>Lorem Ipsum is simply</h5><p>"Lorem Ipsum is simplyLorem Ipsum is simplyLorem Ipsum is simplyLorem Ipsum is simplyLorem Ipsum is simply "</p></div>
    <div class="quote" style="left:164px;top:3191px"><i class="dot"></i><h5>Lorem Ipsum is simply</h5><p>"Lorem Ipsum is simplyLorem Ipsum is simplyLorem Ipsum is simplyLorem Ipsum is simply "</p></div>
    <div class="quote" style="left:132px;top:3306px"><i class="dot"></i><h5>Lorem Ipsum is simply</h5><p>"Lorem Ipsum is simplyLorem Ipsum is simplyLorem Ipsum is simplyLorem Ipsum is simplyLorem Ipsum is simply "</p></div>
    <div class="blog-kicker">Explore more with our</div>
    <h2 class="blog-title">Blog</h2>
    <p class="blog-text">To make choosing much easier for You, we provide the widest possible range of services. Let it be media relations, crisis management or marketing services, our experts are always available.</p>
    <div class="more">MORE <span>→</span></div>
  </section>

  <section class="cta">
    <div class="photo" role="img" aria-label="Faint office scene behind a magenta to red overlay" style="inset:0;background:linear-gradient(90deg,rgba(255,255,255,.04),rgba(255,255,255,.1))"></div>
    <h2>Any questions à Projects?<br>Let's get <em>started.</em></h2>
    <div class="btn btn-white" style="left:346px;width:166px">Send a Message ✎</div>
    <div class="btn btn-grad" style="left:524px;width:131px;border:1px solid rgba(255,255,255,.3)">Get started</div>
  </section>

  <footer class="footer">
    <div class="brand"><i></i>Halcyra</div>
    <div class="fcol" style="left:252px"><h6>About us</h6><ul><li>Lorem Ipsum</li><li>Lorem Ipsum</li><li>Lorem Ipsum</li><li>Lorem Ipsum</li></ul></div>
    <div class="fcol" style="left:387px"><h6>services</h6><ul><li>Lorem Ipsum</li><li>Lorem Ipsum</li><li>Lorem Ipsum</li><li>Lorem Ipsum</li></ul></div>
    <div class="fcol" style="left:521px;top:84px"><div class="small">Toll Free Customer Care</div><div class="big">+(1) 555 014 2290</div><div class="small">Need live support?</div><div class="big">order@halcyra.example</div></div>
    <div class="fcol" style="left:694px"><h6>Follow us</h6><div class="socials"><i></i><i></i><i></i></div></div>
    <div class="fbottom" style="left:132px">English / USD &nbsp;&nbsp;&nbsp;&nbsp;&nbsp; Privacy Policy &nbsp;&nbsp;&nbsp;&nbsp;&nbsp; Contact</div>
    <div class="fbottom" style="left:806px">© 2023 Halcyra</div>
  </footer>
</div>
<div class="scrollbar"><span></span></div>

<div class="mobile">
  <div class="m-hero">
    <div class="brand"><i></i>Halcyra</div>
    <div class="m-burger"></div>
    <div class="k">LOREM IPSUM IS SIMPLY DUMMY</div>
    <h1>Unique<br>digital<br><em>ideas.</em></h1>
    <p>Our experts, creative staff and data analysts are up to the most extraordinary challenges on all parts of the world.</p>
    <div class="btn btn-grad" style="top:222px">Let's Talk →</div>
    <div class="btn btn-white" style="top:246px">Get Started →</div>
    <svg class="abs" style="left:0;bottom:0" width="148" height="24" viewBox="0 0 148 24" preserveAspectRatio="none"><path d="M0 20 C40 8 80 24 148 0 L148 24 L0 24Z" fill="#fff"/></svg>
  </div>
  <div class="photo" role="img" aria-label="Portrait of a smiling businesswoman" style="left:8px;top:342px;width:118px;height:145px;background:linear-gradient(135deg,#f1ede8,#d9cfc4)"></div>
  <div class="m-t" style="top:492px;font-size:15px;line-height:17px">We are<br>building<br>relationships</div>
  <div class="m-h" style="top:560px">Company Benefits</div>
  <div class="m-p" style="top:570px">Thinking beyond media relations and marketing services, we understand the needs of our clients, and our experts work on building long-term relationships.</div>
  <div class="m-h" style="top:623px">Philosophy</div>
  <div class="m-p" style="top:633px">Thinking beyond media relations and marketing services, we understand the needs of our clients and partners.</div>
  <div class="m-h" style="top:680px">Global Solution</div>
  <div class="m-p" style="top:690px">Thinking beyond media relations and marketing services, we understand the needs of our clients and build lasting ties.</div>
  <div class="m-t" style="top:752px;font-size:56px;font-weight:700;line-height:1">9</div>
  <div class="m-p" style="top:840px;font-size:4px">Years of experience</div>
  <div class="badge" style="left:8px;top:853px;font-size:3.5px;padding:2px 4px">Our Expertise</div>
  <div class="m-t" style="top:866px;font-size:11px;line-height:12px;font-weight:400;width:140px">we provide the widest possible range of services.</div>
  <div class="m-p" style="top:915px">To make choosing much easier for You, we provide the widest possible range of services. Let it be media relations, crisis management or marketing services.</div>
  <div class="m-p" style="top:975px">To make choosing much easier for You, we provide the widest possible range of services, our experts are always available.</div>
  <div class="m-li" style="top:1030px;font-size:4px;color:#8a8a95">OUR SERVICES</div>
  <div class="m-li" style="top:1045px;line-height:20.6px">Consumer Products and Services<br>Content &amp; Publishing Strategy<br>Crisis Management<br>Brand Marketing<br>B2B Marketing<br>Change Management</div>
  <div class="m-li" style="top:1170px;font-size:4px;color:#8a8a95">OUR SERVICES</div>
  <div class="m-li" style="top:1180px;line-height:20.6px">Data &amp; Analytics<br>Public Affairs<br>Social Media<br>Media Relation<br>Technology<br>Media Production</div>
  <div class="m-t serif" style="top:1332px;font-size:11px;font-weight:600">Other specialities</div>
  <div class="m-p" style="top:1350px;color:#8a8a95">We provide digital experience services to startups and small businesses.</div>
  <div class="photo" role="img" aria-label="Two business people shaking hands" style="left:8px;top:1401px;width:132px;height:159px;background:linear-gradient(135deg,#2f4f73,#7f9bb8 50%,#c9d6e2)"></div>
  <div class="abs" style="left:8px;top:1572px;width:20px;height:20px;border-radius:50%;background:var(--magenta)"></div>
  <div class="m-h" style="left:36px;top:1570px;color:#16161c">Specialized Pre-Sales</div>
  <div class="m-p" style="left:36px;top:1580px;width:100px;color:#8a8a95">Our experts can offer a wide network of relations, from large corporations.</div>
  <div class="abs" style="left:8px;top:1645px;width:20px;height:20px;border-radius:50%;background:var(--magenta)"></div>
  <div class="m-h" style="left:36px;top:1643px;color:#16161c">Armed Forces</div>
  <div class="m-p" style="left:36px;top:1653px;width:100px;color:#8a8a95">We have shown several solutions made for armed forces that support IT-infrastructure.</div>
  <div class="abs" style="left:8px;top:1727px;width:20px;height:20px;border-radius:50%;background:var(--magenta)"></div>
  <div class="m-h" style="left:36px;top:1725px;color:#16161c">Partnership Management</div>
  <div class="m-p" style="left:36px;top:1735px;width:100px;color:#8a8a95">Partnerships never go out of style. Corporations keep seeking more.</div>
  <div class="m-t" style="left:20px;top:1849px;font-size:7px;line-height:10px;text-align:center;width:108px">Leading the best <span class="serif">marketing team.</span></div>
  <div class="m-card" style="top:1908px"><div class="photo" role="img" aria-label="Portrait of a male team member" style="background:linear-gradient(135deg,#5b7fa6,#3b3a40)"></div><span>Lorem Ipsum is</span></div>
  <div class="m-card" style="top:2066px"><div class="photo" role="img" aria-label="Portrait of a female team member" style="background:linear-gradient(135deg,#f0ece6,#d8ccbf)"></div><span>Lorem Ipsum is</span></div>
  <div class="m-card" style="top:2216px"><div class="photo" role="img" aria-label="Portrait of a male team member in a suit" style="background:linear-gradient(135deg,#e7ecef,#59606a)"></div><span>Lorem Ipsum is</span></div>
  <div class="photo" role="img" aria-label="Colleagues discussing work in an office" style="left:4px;top:2393px;width:140px;height:132px;background:linear-gradient(160deg,#c9cfd6,#7d8794)"></div>
  <div class="m-t" style="top:2425px;left:12px;font-size:7px;line-height:10px;color:#fff;width:60px">Watch the creative process behind the Our work</div>
  <div class="m-q" style="top:2543px">Lorem Ipsum is simply<br>"Lorem Ipsum is simply Lorem Ipsum is simply Lorem Ipsum is simply"</div>
  <div class="m-q" style="top:2603px">Lorem Ipsum is simply<br>"Lorem Ipsum is simply Lorem Ipsum is simply Lorem Ipsum is simply"</div>
  <div class="m-q" style="top:2663px">Lorem Ipsum is simply<br>"Lorem Ipsum is simply Lorem Ipsum is simply Lorem Ipsum is simply"</div>
  <div class="m-p" style="top:2728px;font-size:3.5px">Explore more with our</div>
  <div class="m-t" style="top:2737px;font-size:10px">Blog</div>
  <div class="m-p" style="top:2757px;color:#8a8a95">To make choosing much easier for You, we provide the widest possible range of services. Let it be media relations or crisis management, our experts are always available.</div>
  <div class="abs" style="left:8px;top:2820px;width:28px;height:12px;background:var(--grad);color:#fff;font-size:4px;display:flex;align-items:center;justify-content:center">MORE →</div>
  <div class="m-cta">
    <div class="m-t" style="top:50px;left:10px;width:128px;text-align:center;color:#fff;font-size:8px;line-height:11px">Any questions à Projects? Let's get <span class="serif">started.</span></div>
    <div class="btn btn-white" style="left:28px;top:100px;width:92px;height:13px;font-size:4.5px">Send a Message ✎</div>
    <div class="btn btn-grad" style="left:44px;top:126px;width:60px;height:13px;font-size:4.5px">Get started</div>
  </div>
  <footer class="m-foot">
    <div class="brand" style="left:8px;top:42px;font-size:12px;color:#d83a72"><i style="width:10px;height:10px"></i>Halcyra</div>
    <div class="m-li" style="top:118px;font-size:5px">About us</div>
    <div class="m-li" style="left:76px;top:118px;font-size:5px">services</div>
    <div class="m-li" style="top:132px;font-size:4px;color:#85858f;line-height:8px">Lorem Ipsum<br>Lorem Ipsum<br>Lorem Ipsum<br>Lorem Ipsum</div>
    <div class="m-li" style="left:76px;top:132px;font-size:4px;color:#85858f;line-height:8px">Lorem Ipsum<br>Lorem Ipsum<br>Lorem Ipsum<br>Lorem Ipsum</div>
    <div class="m-li" style="top:180px;font-size:4px;color:#85858f">Toll Free Customer Care</div>
    <div class="m-li" style="top:188px;font-size:5px">+(1) 555 014 2290</div>
    <div class="m-li" style="top:202px;font-size:4px;color:#85858f">Need live support?</div>
    <div class="m-li" style="top:210px;font-size:5px">order@halcyra.example</div>
    <div class="m-li" style="top:228px;font-size:5px">Follow us</div>
    <div class="abs" style="left:8px;top:240px;display:flex;gap:6px"><i style="width:7px;height:7px;border-radius:50%;background:#8a8a93;display:block"></i><i style="width:7px;height:7px;border-radius:50%;background:#8a8a93;display:block"></i><i style="width:7px;height:7px;border-radius:50%;background:#8a8a93;display:block"></i></div>
    <div class="m-li" style="top:258px;font-size:3.5px;color:#85858f">English / USD &nbsp; Privacy Policy &nbsp; Contact</div>
    <div class="m-li" style="top:270px;font-size:3.5px;color:#85858f">© 2023 Halcyra</div>
  </footer>
</div>

</body>
</html>
```